Flyer for Choir Christmas Concert

Need colorful flyer for Christmas Choir Concert.

Requirements
Should not have
• I don't like musical symbols incorporated into the design.

```html
<!DOCTYPE html>
<html lang="en">
<head>
<meta charset="utf-8">
<title>Love &amp; Joy – Silverline Holiday Concert</title>
<link rel="stylesheet" href="https://fonts.googleapis.com/css2?family=Cinzel:wght@600&family=Libre+Baskerville:wght@400;700&family=Arimo&display=swap">
<style>
  :root {
    --red: #c8161d;
    --ink: #2a2a2e;
    --white: #ffffff;
    --snow-top: #d9d8ec;
    --snow-mid: #eeeaf6;
    --snow-low: #f7f5fb;
    --light-glow: #fbe9d6;
  }
  * { box-sizing: border-box; margin: 0; padding: 0; }
  html, body { width: 849px; height: 1200px; overflow: hidden; background: var(--white); }
  .flyer { position: relative; width: 849px; height: 1200px; overflow: hidden; font-family: "Libre Baskerville", Georgia, serif; color: var(--ink); }

  .backdrop {
    position: absolute; left: 0; top: 0; width: 849px; height: 865px;
    background:
      radial-gradient(ellipse 260px 160px at 560px 770px, rgba(40,60,130,0.35), transparent 70%),
      radial-gradient(ellipse 420px 120px at 200px 620px, var(--light-glow), transparent 75%),
      linear-gradient(180deg, var(--snow-top) 0%, var(--snow-mid) 45%, #ece6ef 70%, var(--snow-low) 100%);
  }

  .title {
    position: absolute; top: 66px; left: 0; width: 100%; text-align: center;
    font-family: "Cinzel", "Times New Roman", serif; font-weight: 600;
    font-size: 104px; line-height: 1; color: var(--red);
  }
  .intro {
    position: absolute; top: 205px; left: 0; width: 100%; text-align: center;
    font-weight: 700; font-size: 23.5px; line-height: 31.5px;
  }

  .guests {
    position: absolute; left: 116px; top: 331px; width: 595px; height: 110px;
    border: 2px solid var(--red); text-align: center; padding-top: 2px;
  }
  .guests legend {
    margin: 0 auto; padding: 0 14px;
    color: var(--red); font-weight: 700; font-size: 22px; line-height: 26px;
  }
  .guests p { font-weight: 700; font-size: 22.5px; line-height: 31px; }

  .schedule {
    position: absolute; top: 474px; left: 0; width: 100%; text-align: center;
    font-size: 19px; line-height: 27px;
  }
  .venue { margin-top: 15px; }

  .tickets { position: absolute; left: 112px; top: 625px; width: 206px; height: 210px; }
  .tickets svg { position: absolute; inset: 0; }
  .tickets p {
    position: absolute; left: 0; top: 61px; width: 100%; text-align: center;
    font-size: 13px; line-height: 18px;
  }
  .tickets b { font-weight: 700; }

  .info-band {
    position: absolute; left: 0; top: 865px; width: 849px; height: 88px;
    background: var(--red); color: var(--white); text-align: center; padding-top: 12px;
  }
  .info-band .note { font-size: 23px; line-height: 32px; }
  .info-band .web { font-weight: 700; font-size: 21px; line-height: 30px; }

  .org { position: absolute; top: 1010px; left: 0; width: 100%; text-align: center; }
  .org-name { font-weight: 700; font-size: 38px; line-height: 46px; color: var(--ink); }
  .staff {
    margin-top: 22px; font-family: "Arimo", Arial, sans-serif;
    font-size: 13px; line-height: 18px; color: var(--ink);
  }
  .legal {
    position: absolute; top: 1136px; left: 0; width: 100%; text-align: center;
    font-family: "Arimo", Arial, sans-serif; font-size: 8.5px; color: var(--ink);
  }
</style>
</head>
<body>
<main class="flyer">
  <div class="backdrop" role="img" aria-label="Soft photograph of a blue and a white Christmas ornament resting in snow, with glowing bokeh lights behind"></div>

  <h1 class="title">Love &amp; Joy</h1>
  <p class="intro">Join the singers of Silverline as we<br>perform carols, chorales, and other joyful and<br>poignant music of the season!</p>

  <fieldset class="guests">
    <legend>WITH SPECIAL GUESTS</legend>
    <p>The Choirs of Maple Ridge Middle School<br>Evan Rowe, director</p>
  </fieldset>

  <div class="schedule">
    <p>Saturday, December 1 at 5:00pm<br>Sunday, December 2 at 3:00pm</p>
    <p class="venue">Grace Hill Community Church<br>1480 Juniper Avenue NE Albuquerque</p>
  </div>

  <div class="tickets">
    <svg viewBox="0 0 180 200" width="206" height="210" preserveAspectRatio="none" aria-hidden="true">
      <path fill="none" stroke="#c8161d" stroke-width="2"
        d="M166 100 A20 20 0 0 1 158.5 139.1 A20 20 0 0 1 137.3 170.4 A20 20 0 0 1 106.9 187.8 A20 20 0 0 1 73.1 187.8 A20 20 0 0 1 42.7 170.4 A20 20 0 0 1 21.5 139.1 A20 20 0 0 1 14 100 A20 20 0 0 1 21.5 60.9 A20 20 0 0 1 42.7 29.6 A20 20 0 0 1 73.1 12.2 A20 20 0 0 1 106.9 12.2 A20 20 0 0 1 137.3 29.6 A20 20 0 0 1 158.5 60.9 A20 20 0 0 1 166 100 Z"/>
    </svg>
    <p>Tickets available<br>Online and at the door:<br>General <b>$20</b><br>Seniors <b>$15</b><br>Students <b>$10</b></p>
  </div>

  <section class="info-band">
    <p class="note">Complimentary childcare provided at both performances</p>
    <p class="web">www.silverline-choir.org</p>
  </section>

  <footer class="org">
    <p class="org-name">Silverline Choral Artists</p>
    <p class="staff">Daniel Marsh, Artistic Director<br>Rosa Delgado Finch, Executive Director</p>
  </footer>
  <p class="legal">Silverline is a 501(c)3 non-profit organization, and an Ensemble-in-Residence at Grace Hill Community Church</p>
</main>
</body>
</html>
```